Need Business Cards for my Business

email address: rkpmarlowhollowworks@vendrimail.com
web address: rkpmarlowhollowworks.net
Slogan: We offer various QVN licenses
Rowland K. Pemberly
Please stick with colors of Company Logo
would like the card to be more of the color example of the logo.
If you need PDF copy of logo email me at the above account.
Creative control rests with you.

Industry/Entity Type

Business

Contact Information for Business Card

I am a minimalist, but would like something to pop and stand out amongst other cards, make it memorable.

Font styles to use
Serif
Decorative
Script

```html
<!DOCTYPE html>
<html lang="en">
<head>
<meta charset="utf-8">
<title>RKP Marlow Hollow Works — Business Card</title>
<link rel="stylesheet" href="https://fonts.googleapis.com/css2?family=Exo+2:wght@700&family=Montserrat:wght@400;500&family=Mulish:wght@400;800&display=swap">
<style>
  :root {
    --backdrop: #222222;
    --blue-top: #1b6aa8;
    --blue-bottom: #173f6b;
    --navy: #1c3a63;
    --red: #e5252d;
    --ink: #25303d;
    --white: #ffffff;
  }
  * { margin: 0; padding: 0; box-sizing: border-box; }
  html, body {
    width: 1189px; height: 1200px; overflow: hidden;
    background: var(--backdrop);
  }
  .stage {
    position: absolute; left: 0; top: 0;
    width: 1457px; height: 1470px;
    transform: scale(0.8161); transform-origin: 0 0;
  }
  .card {
    position: absolute; left: 210px;
    width: 1048px; height: 598px;
    overflow: hidden;
  }
  .card--front {
    top: 82px;
    background: linear-gradient(180deg, var(--blue-top), var(--blue-bottom));
    color: var(--white);
  }
  .card--back { top: 767px; background: var(--white); }

  .brand-name {
    font-family: "Exo 2", sans-serif; font-weight: 700;
    letter-spacing: 2px; line-height: 1.05;
  }
  .slogan {
    font-family: "Montserrat", sans-serif; font-weight: 400;
    font-size: 25px; letter-spacing: 4.2px; white-space: nowrap;
  }
  .card--front .brand-block {
    position: absolute; left: 268px; top: 205px; width: 520px;
    text-align: left;
  }
  .card--front .brand-name { font-size: 62px; color: var(--white); }
  .card--front .slogan { margin-top: 22px; color: var(--white); }

  .card--back .brand-block { position: absolute; left: 56px; top: 62px; }
  .card--back .brand-name { font-size: 66px; color: var(--navy); }
  .card--back .slogan { margin-top: 18px; color: var(--red); }

  .swoosh { position: absolute; inset: 0; width: 1048px; height: 598px; }

  .person-name {
    position: absolute; left: 56px; top: 376px;
    font-family: "Mulish", sans-serif; font-weight: 800;
    font-size: 34px; color: var(--ink); letter-spacing: 0.5px;
  }
  .contact-list { position: absolute; left: 56px; top: 452px; list-style: none; }
  .contact-item {
    display: flex; align-items: center; gap: 8px; height: 35px;
    font-family: "Mulish", sans-serif; font-weight: 400;
    font-size: 28px; color: var(--ink);
  }
  .contact-icon { width: 29px; height: 29px; flex: none; }
</style>
</head>
<body>
<div class="stage">

  <section class="card card--front">
    <div class="brand-block">
      <div class="brand-name">RKP MARLOW<br>HOLLOW WORKS</div>
      <div class="slogan">We offer various QVN licenses</div>
    </div>
  </section>

  <section class="card card--back">
    <svg class="swoosh" viewBox="0 0 1048 598" aria-hidden="true">
      <defs>
        <linearGradient id="bandBlue" x1="0" y1="0" x2="0" y2="1">
          <stop offset="0" stop-color="#1b6aa8"/>
          <stop offset="1" stop-color="#173f6b"/>
        </linearGradient>
      </defs>
      <path d="M848 0 H1048 V598 H843 C930 500 968 300 848 0 Z" fill="url(#bandBlue)"/>
      <path d="M930 282 C920 430 800 560 635 598 H830 C898 510 935 400 930 282 Z" fill="var(--red)"/>
    </svg>

    <div class="brand-block">
      <div class="brand-name">RKP MARLOW<br>HOLLOW WORKS</div>
      <div class="slogan">We offer various QVN licenses</div>
    </div>

    <div class="person-name">ROWLAND K. PEMBERLY</div>

    <ul class="contact-list">
      <li class="contact-item">
        <svg class="contact-icon" viewBox="0 0 29 29" aria-hidden="true">
          <rect width="29" height="29" fill="var(--red)"/>
          <path d="M6 12 Q14.5 5 23 12 L20 14 L18 11 H11 L9 14 Z M9 15 H20 L22 22 H7 Z" fill="#fff"/>
        </svg>
        555-014-2286
      </li>
      <li class="contact-item">
        <svg class="contact-icon" viewBox="0 0 29 29" aria-hidden="true">
          <rect width="29" height="29" fill="var(--red)"/>
          <rect x="5" y="8" width="19" height="13" fill="none" stroke="#fff" stroke-width="1.8"/>
          <path d="M5 8 L14.5 16 L24 8 M5 21 L12 14 M24 21 L17 14" fill="none" stroke="#fff" stroke-width="1.6"/>
        </svg>
        rkpmarlowhollowworks@vendrimail.com
      </li>
      <li class="contact-item">
        <svg class="contact-icon" viewBox="0 0 29 29" aria-hidden="true">
          <rect width="29" height="29" fill="var(--red)"/>
          <g fill="none" stroke="#fff" stroke-width="1.5">
            <circle cx="14.5" cy="14.5" r="9"/>
            <ellipse cx="14.5" cy="14.5" rx="4" ry="9"/>
            <path d="M5.5 14.5 H23.5 M7 10 H22 M7 19 H22"/>
          </g>
        </svg>
        rkpmarlowhollowworks.net
      </li>
    </ul>
  </section>

</div>
</body>
</html>
```